Page hosted on godaddy.com, Website domain is dalworth4kiva.com

Page should be based on design of my campaign flyer. I will put all text inside pages, they can be layout with top navigation and bottom header that contains contact information. Pages should be white background

I will use html to edit, or I can also get an editor if you specify which one your design is compatible with

Items listed below that are underlined are actual HTML pages
Total number of pages (including BLOG) = 18

Site Structure

HOME
Blog – should be a wordpress blog inside this page
KIVA Board
• Why I am running
• About Me
• How to vote
Automotive
• My Automotive Career
• Automotive for Fun
• Specialty car brokerage
Aviation
• Aviation Experience
• My Favorite Aviation Projects
• Aviation Sales Business
Other Experience
• My Complete Timeline
• Entrepreneurial Activities
• Dalworth Orchard
• Commercial Development
• Home Construction
• Education
Photos
Updates

update, I would ideally like to use wordpress for the site design.

```html
<!DOCTYPE html>
<html lang="en">
<head>
<meta charset="utf-8">
<title>Dalworth for KIVA</title>
<link href="https://fonts.googleapis.com/css2?family=Poppins:wght@300;400;500&family=Syncopate:wght@700&display=swap" rel="stylesheet">
<style>
:root{
  --red:#c4232b;
  --red-deep:#a81b22;
  --ink:#111111;
  --muted:#8a8a8a;
  --date-ink:#444444;
  --line:#e3e3e3;
  --white:#ffffff;
  --display:"Syncopate", sans-serif;
  --body:"Poppins", sans-serif;
}
*{margin:0;padding:0;box-sizing:border-box}
html,body{width:1200px;height:2914px;overflow:hidden;background:var(--white);font-family:var(--body)}
.page{position:relative;width:1200px;height:2914px}

.hero{position:absolute;left:0;top:0;width:1200px;height:470px;background:linear-gradient(120deg,#b51f27 0%,#cf2a30 45%,#b8262c 100%)}
.site-logo{position:absolute;left:113px;top:20px;color:var(--white);font-family:var(--display);font-size:17px;line-height:24px;letter-spacing:1px}
.main-nav{position:absolute;top:34px;left:0;width:1200px;height:22px}
.main-nav a{position:absolute;color:var(--white);font-size:14.5px;text-decoration:none;white-space:nowrap}
.main-nav .has-sub::after{content:"";display:inline-block;margin-left:6px;vertical-align:middle;border-left:4px solid transparent;border-right:4px solid transparent;border-top:5px solid var(--white)}
.hero-kicker{position:absolute;top:151px;width:1200px;text-align:center;color:var(--white);font-family:var(--display);font-size:17px;letter-spacing:1px}
.hero-title{position:absolute;top:180px;width:1200px;text-align:center;color:var(--white);font-family:var(--display);font-size:39px;letter-spacing:1px}

.content-card{position:absolute;left:111px;top:322px;width:978px;height:2294px;background:var(--white);box-shadow:0 20px 60px rgba(0,0,0,.12)}

.entry{position:absolute;left:0;width:978px;height:407px}
.entry-photo{position:absolute;left:54px;top:0;width:185px;height:189px;background:var(--white);padding:5px;box-shadow:0 2px 10px rgba(0,0,0,.15)}
.entry-photo .fill{width:100%;height:100%}
.entry-day{position:absolute;left:54px;top:212px;width:185px;text-align:center;color:var(--red);font-family:var(--display);font-size:40px;line-height:44px}
.entry-month{position:absolute;left:54px;top:262px;width:185px;text-align:center;color:var(--date-ink);font-size:15.5px}
.entry-rule{position:absolute;left:274px;top:5px;width:1px;height:334px;background:var(--line)}
.entry-rule::before{content:"";position:absolute;left:-6px;top:0;width:13px;height:13px;border-radius:50%;background:var(--red)}
.entry-title{position:absolute;left:310px;top:-2px;color:var(--ink);font-family:var(--display);font-size:28px;line-height:34px;white-space:nowrap}
.entry-text{position:absolute;left:310px;top:46px;width:614px;color:var(--muted);font-size:15.6px;font-weight:300;line-height:25.7px}
.entry-button{position:absolute;left:310px;top:275px;width:190px;height:54px;background:var(--red);border-radius:3px;color:var(--white);font-family:var(--display);font-size:14px;line-height:54px;text-align:center;text-decoration:none}

.pager{position:absolute;top:1682px;left:0}
.pager a{position:absolute;top:0;height:44px;border:1px solid var(--red);color:var(--ink);font-size:15px;line-height:42px;text-align:center;text-decoration:none}
.pager a.current{background:var(--red);color:var(--white)}

.gallery-title{position:absolute;top:1792px;width:978px;text-align:center;color:var(--ink);font-family:var(--display);font-size:29px}
.gallery-grid{position:absolute;left:67px;top:1870px;width:827px;height:352px}
.gallery-grid .tile{position:absolute}

.site-footer{position:absolute;left:0;top:2616px;width:1200px;height:298px}
.footer-logo{position:absolute;top:96px;width:1200px;text-align:center;color:var(--red-deep);font-family:var(--display);font-size:24px}
.social{position:absolute;top:190px;left:532px;width:136px;height:16px}
.social span{position:absolute;top:0;width:14px;height:14px;border-radius:50%;background:#444}
.copyright{position:absolute;top:226px;width:1200px;text-align:center;color:#555;font-size:14.5px}
</style>
</head>
<body>
<div class="page">

  <header class="hero" role="img" aria-label="Red-toned photo of a sedan parked on grass">
    <div class="site-logo">DALWORTH<br>FOR KIVA</div>
    <nav class="main-nav">
      <a style="left:356px">Home</a>
      <a style="left:439px">Blog</a>
      <a style="left:509px">KIVA Board</a>
      <a class="has-sub" style="left:627px">Automotive</a>
      <a class="has-sub" style="left:761px">Aviation</a>
      <a class="has-sub" style="left:871px">Other Experience</a>
      <a style="left:1043px">Photos</a>
    </nav>
    <p class="hero-kicker">WELCOME TO</p>
    <h1 class="hero-title">DALWORTH FOR KIVA</h1>
  </header>

  <main class="content-card">

    <article class="entry" style="top:63px">
      <div class="entry-photo"><div class="fill" role="img" aria-label="Twin-engine airplane in flight over farmland" style="background:linear-gradient(180deg,#8b8f8c 0%,#9a9a8e 55%,#6f6a4e 100%)"></div></div>
      <div class="entry-day">05</div>
      <div class="entry-month">April&nbsp; 2022</div>
      <div class="entry-rule"></div>
      <h2 class="entry-title">ABOUT ME</h2>
      <p class="entry-text">Lorem ipsum dolor sit amet, consectetur adipiscing elit, sed do eiusmod tempor incididunt ut labore et dolore magna aliqua. Quis ipsum suspendisse ultrices gravida. Risus commodo viverra maecenas accumsan lacus vel facilisis. Lorem ipsum dolor sit amet, consectetur adipiscing elit, sed do eiusmod tempor incididunt ut labore et dolore magna aliqua. Quis ipsum suspendisse ultrices gravida. Risus commodo viverra maecenas accumsan lacus vel facilisis. Lorem ipsum dolor sit amet, consectetur adipiscing elit, sed do eiusmod tempor incididunt ut labore et dolore magna aliqua.</p>
      <a class="entry-button">LEARN MORE</a>
    </article>

    <article class="entry" style="top:470px">
      <div class="entry-photo"><div class="fill" role="img" aria-label="Dragster on a race strip under a cloudy sky" style="background:linear-gradient(180deg,#a9c4e4 0%,#d8e0ea 45%,#5d5f63 70%,#2e2f33 100%)"></div></div>
      <div class="entry-day">05</div>
      <div class="entry-month">April&nbsp; 2022</div>
      <div class="entry-rule"></div>
      <h2 class="entry-title">MY AUTOMOTIVE CAREER</h2>
      <p class="entry-text">Lorem ipsum dolor sit amet, consectetur adipiscing elit, sed do eiusmod tempor incididunt ut labore et dolore magna aliqua. Quis ipsum suspendisse ultrices gravida. Risus commodo viverra maecenas accumsan lacus vel facilisis. Lorem ipsum dolor sit amet, consectetur adipiscing elit, sed do eiusmod tempor incididunt ut labore et dolore magna aliqua. Quis ipsum suspendisse ultrices gravida. Risus commodo viverra maecenas accumsan lacus vel facilisis. Lorem ipsum dolor sit amet, consectetur adipiscing elit, sed do eiusmod tempor incididunt ut labore et dolore magna aliqua.</p>
      <a class="entry-button">LEARN MORE</a>
    </article>

    <article class="entry" style="top:877px">
      <div class="entry-photo"><div class="fill" role="img" aria-label="Engine bay of a performance car" style="background:linear-gradient(160deg,#9a9a9a 0%,#3a3a3c 45%,#555 75%,#b9b9b9 100%)"></div></div>
      <div class="entry-day">05</div>
      <div class="entry-month">April&nbsp; 2022</div>
      <div class="entry-rule"></div>
      <h2 class="entry-title">AVIATION EXPERIENCE</h2>
      <p class="entry-text">Lorem ipsum dolor sit amet, consectetur adipiscing elit, sed do eiusmod tempor incididunt ut labore et dolore magna aliqua. Quis ipsum suspendisse ultrices gravida. Risus commodo viverra maecenas accumsan lacus vel facilisis. Lorem ipsum dolor sit amet, consectetur adipiscing elit, sed do eiusmod tempor incididunt ut labore et dolore magna aliqua. Quis ipsum suspendisse ultrices gravida. Risus commodo viverra maecenas accumsan lacus vel facilisis. Lorem ipsum dolor sit amet, consectetur adipiscing elit, sed do eiusmod tempor incididunt ut labore et dolore magna aliqua.</p>
      <a class="entry-button">LEARN MORE</a>
    </article>

    <article class="entry" style="top:1284px">
      <div class="entry-photo"><div class="fill" role="img" aria-label="Private jet parked on an airfield apron" style="background:linear-gradient(180deg,#2f73c4 0%,#6ea3da 50%,#6c8a4a 70%,#a3a3a0 100%)"></div></div>
      <div class="entry-day">05</div>
      <div class="entry-month">April&nbsp; 2022</div>
      <div class="entry-rule"></div>
      <h2 class="entry-title">COMMERCIAL DEVELOPMENT</h2>
      <p class="entry-text">Lorem ipsum dolor sit amet, consectetur adipiscing elit, sed do eiusmod tempor incididunt ut labore et dolore magna aliqua. Quis ipsum suspendisse ultrices gravida. Risus commodo viverra maecenas accumsan lacus vel facilisis. Lorem ipsum dolor sit amet, consectetur adipiscing elit, sed do eiusmod tempor incididunt ut labore et dolore magna aliqua. Quis ipsum suspendisse ultrices gravida. Risus commodo viverra maecenas accumsan lacus vel facilisis. Lorem ipsum dolor sit amet, consectetur adipiscing elit, sed do eiusmod tempor incididunt ut labore et dolore magna aliqua.</p>
      <a class="entry-button">LEARN MORE</a>
    </article>

    <nav class="pager">
      <a class="current" style="left:89px;width:47px">1</a>
      <a style="left:146px;width:45px">2</a>
      <a style="left:200px;width:45px">3</a>
      <a style="left:257px;width:80px">Next</a>
    </nav>

    <h2 class="gallery-title">OUR GALLERY</h2>
    <div class="gallery-grid">
      <div class="tile" role="img" aria-label="Black sedan parked on a gravel drive among trees" style="left:0;top:0;width:362px;height:352px;background:linear-gradient(180deg,#3f5a2c 0%,#6a7d45 45%,#a79e8c 75%,#8f8676 100%)"></div>
      <div class="tile" role="img" aria-label="Pilot and passenger inside a small aircraft cockpit" style="left:368px;top:0;width:225px;height:172px;background:linear-gradient(135deg,#c9c6c0 0%,#8e8b86 50%,#4b4a48 100%)"></div>
      <div class="tile" role="img" aria-label="Supercharged engine under an open hood" style="left:601px;top:0;width:226px;height:172px;background:linear-gradient(160deg,#8fa04e 0%,#3a3a3c 40%,#5a5a5c 80%,#a7a7a7 100%)"></div>
      <div class="tile" role="img" aria-label="Engine block cylinders on a workbench" style="left:368px;top:180px;width:225px;height:172px;background:linear-gradient(180deg,#bdbdbd 0%,#6b6b6b 50%,#cfcfcf 100%)"></div>
      <div class="tile" role="img" aria-label="Group gathered at an indoor car show" style="left:601px;top:180px;width:226px;height:172px;background:linear-gradient(180deg,#6e6a55 0%,#2f3438 55%,#1f2326 100%)"></div>
    </div>

  </main>

  <footer class="site-footer">
    <div class="footer-logo">DALWORTH FOR KIVA</div>
    <div class="social" aria-label="Social links">
      <span style="left:0"></span>
      <span style="left:30px"></span>
      <span style="left:60px"></span>
      <span style="left:90px"></span>
      <span style="left:120px"></span>
    </div>
    <p class="copyright">©Copyrights 2022 Dalworth For Kiva &nbsp; | &nbsp; All Rights Reserved</p>
  </footer>

</div>
</body>
</html>
```